Stonefield Partners Business Card Design

We are looking for a new business card design, we are not happy with our current design. We are a boutique management consulting firm and our clients are typically fortune 500 companies.

I have attached the current front and back that we have as well as a version of our logo that can be used. I am trying to get a higher resolution version of the logo file to upload to the project.

Target Market(s)

Fortune 500 companies are our primary client base. Financial services, life sciences, pharmaceuticals and telecom companies are

Industry/Entity Type

Management Consulting

Contact Information for Business Card

We are trying to communicate a high degree of professionalism, a somewhat minimalist perhaps with some air of whimsy (without overdoing it). Attached is the current design, front and back as well as logos. I like the current back of the card and assume we will keep the phrase the same.

From a color palette perspective, I prefer to stay with a gray scale as they are today.

Font styles to use
Sans Serif

Colors
1b1b1b
474747
ffffff

Requirements
Must have
• Two sided business card design. File format should be something that can be used outside of Photoshop like MS Publisher so that they can be edited with personal information.
• Font should be calibri or something very similar and should be available within MS Office
Should not have
• No other logos or graphics outside of the logo provided.

```html
<!DOCTYPE html>
<html lang="en">
<head>
<meta charset="utf-8">
<title>Stonefield Partners Business Card</title>
<link href="https://fonts.googleapis.com/css2?family=Carlito:wght@400;700&display=swap" rel="stylesheet">
<style>
  :root {
    --ink: #1b1b1b;
    --graphite: #474747;
    --paper: #ffffff;
    --stage: #e6e6e6;
    --soft: #bdbdbd;
  }
  * { margin: 0; padding: 0; box-sizing: border-box; }
  html, body { width: 1200px; height: 1023px; overflow: hidden; }
  body {
    background: var(--stage);
    font-family: "Carlito", "Calibri", sans-serif;
    position: relative;
  }
  .card {
    position: absolute;
    left: 215px;
    width: 770px;
    height: 440px;
    border-radius: 22px;
    overflow: hidden;
  }
  .card--front {
    top: 50px;
    background: radial-gradient(circle at 40% 30%, #4a4a4a 0%, var(--ink) 70%);
    color: var(--paper);
  }
  .card--back {
    top: 533px;
    background: linear-gradient(135deg, var(--paper) 0%, #ececec 100%);
    color: var(--ink);
    box-shadow: 0 0 0 1px #d0d0d0;
  }
  .brand {
    position: absolute;
    left: 48px;
    top: 58px;
    display: flex;
    align-items: center;
    gap: 18px;
  }
  .brand__dot {
    width: 46px; height: 46px;
    border-radius: 50%;
    background: var(--paper);
  }
  .brand__name {
    font-size: 84px;
    font-weight: 400;
    line-height: 1;
    letter-spacing: -1px;
  }
  .brand__tm { font-size: 14px; align-self: flex-start; margin-left: -12px; }
  .divider {
    position: absolute;
    left: 48px; right: 48px; top: 258px;
    height: 2px;
    background: var(--paper);
    opacity: .85;
  }
  .person {
    position: absolute;
    left: 48px; top: 222px;
    font-size: 28px; font-weight: 700;
  }
  .person__title { font-size: 16px; font-weight: 400; }
  .company {
    position: absolute;
    right: 48px; top: 222px;
    font-size: 28px; font-weight: 700;
  }
  .details {
    position: absolute;
    top: 274px;
    font-size: 20px;
    line-height: 1.5;
    color: #e8e8e8;
  }
  .details--office { left: 48px; }
  .details--hq { right: 48px; text-align: right; }
  .details__row { display: flex; align-items: center; gap: 8px; }
  .details--hq .details__row { justify-content: flex-end; }
  .icon { width: 18px; height: 18px; flex: none; }
  .website {
    position: absolute;
    left: 40px; top: 50%;
    transform: translate(-50%, -50%) rotate(90deg) translateY(-60px);
    font-size: 20px;
    letter-spacing: 3px;
    color: var(--ink);
    white-space: nowrap;
  }
  .back-brand {
    position: absolute;
    left: 230px; top: 175px;
    display: flex; align-items: center; gap: 22px;
  }
  .back-brand__dot {
    width: 60px; height: 60px; border-radius: 50%;
    background: var(--ink);
  }
  .back-brand__name { font-size: 72px; line-height: 1; }
</style>
</head>
<body>

<section class="card card--front">
  <div class="brand">
    <span class="brand__dot"></span>
    <span class="brand__name">Stonefield</span>
    <span class="brand__tm">TM</span>
  </div>

  <div class="person">Mark Ellison, <span class="person__title">Managing Director</span></div>
  <div class="company">Stonefield Partners, Inc.</div>
  <div class="divider"></div>

  <div class="details details--office">
    <div class="details__row">Los Angeles Office</div>
    <div class="details__row">
      <svg class="icon" viewBox="0 0 20 20"><circle cx="10" cy="10" r="8.5" fill="none" stroke="#fff" stroke-width="1.5"/><path d="M7 6c0 4 3 7 7 7l-1.5-2-1.5.5c-1-.5-2-1.5-2.5-2.5l.5-1.5z" fill="#fff"/></svg>
      503-555-0142
    </div>
    <div class="details__row">
      <svg class="icon" viewBox="0 0 20 20"><rect x="2" y="5" width="16" height="11" fill="#fff"/><path d="M2 5l8 6 8-6" fill="none" stroke="#1b1b1b" stroke-width="1.3"/></svg>
      mellison@stonefieldpartners.com
    </div>
  </div>

  <div class="details details--hq">
    <div class="details__row">
      Headquarters
      <svg class="icon" viewBox="0 0 20 20"><path d="M10 2a6 6 0 0 0-6 6c0 4.5 6 10 6 10s6-5.5 6-10a6 6 0 0 0-6-6z" fill="#fff"/><circle cx="10" cy="8" r="2.2" fill="#1b1b1b"/></svg>
    </div>
    <div class="details__row">712 Alder Crest Avenue</div>
    <div class="details__row">Suite 204, Cedarbrook, OR 97035</div>
  </div>
</section>

<section class="card card--back">
  <div class="website">www.stonefieldpartners.com</div>
  <div class="back-brand">
    <span class="back-brand__dot"></span>
    <span class="back-brand__name">Stonefield</span>
  </div>
</section>

</body>
</html>
```